Website needed for Entertainment Company [Wordpress & Mobile Site] (Contest)

"Tumble Scholars" does Acrobatic Educational Shows for schools.
We need a 4-Page Wordpress site, for BOTH Desktop & Mobile
THINGS WE'D LIKE ON THE HOME PAGE
- Book Now buttons
- Panel advertising "Kindness-Shield Tumbling Tour" with subheading "Educating the Victim, Empowering the Bystander, and Enlightening the Bully" with Photo & 'Read More'
- text somewhere saying "Tumble Scholars engages children in important topics, by utilising Parkour & Acrobatics to captivate and enthrall todays youngest generation."
- Panel advertising Teachers Resources: "Curriculum based resources for teachers including lesson plans, workbooks, and physical activities for before & after the show." Maybe even some boxes that say a subject that is covered (eg. Mathematics. Science. PD/H/PE.)
- Everything else that you recommend
4 PAGES:
- Home Page
- About Us
- Our Program & Shows
- Teachers Resources Portal
NOTE: Transparent & Source files for logo will be provided soon (recently finished being designed)

```html
<!DOCTYPE html>
<html lang="en">
<head>
<meta charset="utf-8">
<title>Tumble Scholars — Acrobatic Educational Shows</title>
<link href="https://fonts.googleapis.com/css2?family=Open+Sans:wght@400;600;700&display=swap" rel="stylesheet">
<style>
  :root{
    --green:#3cb34a;
    --green-soft:#eaf6ec;
    --ink:#2e2e2e;
    --muted:#8a8a8a;
    --line:#e6e6e6;
    --paper:#ffffff;
    --grey-bg:#f6f7f8;
    --footer-bg:#fafafa;
    --brand:#f29a1f;
    --dark-btn:#4a4f55;
  }
  *{box-sizing:border-box;margin:0;padding:0}
  html,body{width:1200px;height:2416px;overflow:hidden}
  body{font-family:"Open Sans",Arial,sans-serif;color:var(--ink);background:var(--paper);position:relative}
  .btn{display:inline-block;background:var(--green);color:#fff;font-weight:700;font-size:15px;letter-spacing:.5px;padding:12px 26px;border-radius:3px;text-decoration:none}
  .btn-sm{font-size:12px;padding:9px 20px}
  .green{color:var(--green)}

  /* header */
  .site-header{position:absolute;top:0;left:0;width:1200px;height:80px;display:flex;align-items:center;padding:0 100px;justify-content:space-between}
  .brand{display:flex;align-items:center;gap:10px;color:var(--brand);font-weight:700;font-size:22px}
  .brand-dot{width:22px;height:22px;border-radius:50%;background:var(--brand)}
  .main-nav{display:flex;align-items:center;gap:30px;font-size:13px;color:#555}
  .phone-btn{background:var(--green);color:#fff;font-weight:700;font-size:12px;padding:7px 14px;border-radius:3px}

  /* hero */
  .hero{position:absolute;top:80px;left:0;width:1200px;height:500px;text-align:center}
  .hero-kicker{margin-top:60px;font-size:22px;color:#444}
  .hero-title{font-size:44px;font-weight:700;margin-top:6px;color:#333}
  .hero .btn{margin-top:24px}
  .city-band{position:absolute;left:0;bottom:0;width:1200px;height:260px;background:linear-gradient(180deg,#ffffff 0%,#e9ecef 45%,#cfd6dd 80%,#9aa3ab 92%,#6d757c 100%)}

  /* intro + tour */
  .intro{position:absolute;top:600px;left:0;width:1200px;height:460px}
  .intro-bg{position:absolute;left:0;top:300px;width:1200px;height:160px}
  .intro-left{position:absolute;left:150px;top:40px;width:400px}
  .section-h{font-size:34px;font-weight:700}
  .body-text{font-size:13px;line-height:1.6;color:var(--muted);margin-top:10px}
  .checks{list-style:none;margin-top:14px}
  .checks li{display:flex;align-items:center;gap:10px;font-size:13px;color:#555;margin-bottom:10px}
  .tick{width:18px;height:18px;border-radius:50%;background:var(--green);display:flex;align-items:center;justify-content:center}
  .show-art{margin-top:12px;width:360px;height:140px;border-radius:6px;background:linear-gradient(135deg,#e8f3fb,#d7e7f2 60%,#f3e4d2)}
  .tour-card{position:absolute;left:620px;top:20px;width:420px;height:420px;background:#fff;box-shadow:0 6px 28px rgba(0,0,0,.14);padding:34px 40px}
  .tour-card .label{font-size:16px;color:#555}
  .tour-card .product{font-size:38px;font-weight:700;color:var(--green);line-height:1.15;margin-top:2px}
  .tour-card .sub{font-size:14px;font-weight:600;color:#444;line-height:1.5;margin-top:10px}
  .tour-card .btn{margin-top:18px}

  /* steps */
  .steps{position:absolute;top:1110px;left:0;width:1200px;height:520px;text-align:center}
  .steps-title{font-size:46px;font-weight:700;margin-top:50px}
  .steps-sub{font-size:20px;color:var(--green);margin-top:2px}
  .step-row{display:flex;justify-content:center;gap:40px;margin-top:60px;align-items:flex-start}
  .step{width:280px;padding:24px 20px}
  .step.featured{background:#fff;box-shadow:0 6px 26px rgba(0,0,0,.13);margin-top:-30px;padding-top:34px;padding-bottom:34px}
  .step-art{width:150px;height:100px;margin:0 auto;border-radius:6px;background:linear-gradient(135deg,#e9eef3,#d3dde6)}
  .step-no{font-size:10px;color:var(--green);letter-spacing:1px;margin-top:16px;font-weight:600}
  .step-name{font-size:17px;font-weight:700;margin-top:4px}
  .step .body-text{font-size:12px}

  /* teachers resources */
  .resources{position:absolute;top:1660px;left:0;width:1200px;height:340px;background:var(--grey-bg)}
  .browser{position:absolute;left:150px;top:-24px;width:400px;height:270px;background:#fff;box-shadow:0 6px 24px rgba(0,0,0,.14)}
  .browser-bar{height:22px;background:#e9ecef;display:flex;align-items:center;gap:6px;padding:0 10px}
  .browser-bar span{width:8px;height:8px;border-radius:50%;background:#c7ccd1}
  .browser-nav{height:20px;background:#fff;display:flex;align-items:center;padding:0 10px;font-size:11px;font-weight:700;color:var(--green)}
  .resource-photos{margin:8px 10px;height:208px;border-radius:3px;background:linear-gradient(135deg,#c7b8a2,#8f9fae 50%,#56687a)}
  .plant{position:absolute;left:100px;top:200px;width:80px;height:120px;border-radius:40px 40px 6px 6px;background:linear-gradient(180deg,#4aa64f,#2f7f3a)}
  .resources-text{position:absolute;left:660px;top:70px;width:420px}
  .resources-text .section-h{font-size:30px;font-weight:600}
  .subjects{display:flex;gap:8px;margin-top:14px}
  .subjects span{font-size:11px;font-weight:600;color:var(--green);border:1px solid var(--green);border-radius:3px;padding:4px 10px;background:#fff}
  .resources-text .btn{margin-top:16px}

  /* footer */
  .site-footer{position:absolute;top:2020px;left:0;width:1200px;height:360px;background:var(--footer-bg);border-top:1px solid var(--line)}
  .footer-col{position:absolute;top:70px}
  .footer-about{left:150px;width:320px}
  .footer-about .brand{font-size:26px}
  .footer-about .body-text{font-size:12px}
  .btn-dark{background:var(--dark-btn);margin-top:18px;font-size:13px;padding:10px 26px}
  .socials{display:flex;gap:8px;margin-top:22px}
  .socials span{width:24px;height:24px;border-radius:50%;background:#6a7077}
  .footer-h{font-size:14px;font-weight:700;margin-bottom:14px}
  .footer-contact{left:540px;width:240px;top:80px}
  .contact-row{display:flex;gap:10px;font-size:11px;color:#666;line-height:1.6;margin-bottom:12px}
  .contact-row svg{flex:none;margin-top:2px}
  .footer-sitemap{left:820px;width:260px;top:80px}
  .sitemap{display:grid;grid-template-columns:1fr 1fr;gap:6px 20px;list-style:none;font-size:11px;color:#666}
  .bottom-bar{position:absolute;top:2380px;left:0;width:1200px;height:36px;border-top:1px solid var(--line);display:flex;align-items:center;justify-content:space-between;padding:0 440px;font-size:10px;color:#888}
</style>
</head>
<body>

<header class="site-header">
  <div class="brand"><span class="brand-dot"></span>Tumble Scholars</div>
  <nav class="main-nav">
    <span>Home</span><span>About Us</span><span>Shows</span><span>Resources</span><span>Contact Us</span>
    <span class="phone-btn">+1 555 014 2290</span>
  </nav>
</header>

<section class="hero">
  <p class="hero-kicker">Acrobatic Educational Shows</p>
  <h1 class="hero-title"><span class="green">Learning</span> Through Parkour &amp; Acrobatics.</h1>
  <a class="btn" href="#">BOOK NOW! &rarr;</a>
  <div class="city-band" role="img" aria-label="Flat illustration of a town skyline with schools, trees and cars on a road"></div>
</section>

<section class="intro">
  <svg class="intro-bg" viewBox="0 0 1200 160" preserveAspectRatio="none" aria-hidden="true">
    <path d="M0 60 L600 0 L1200 70 L1200 160 L0 160 Z" fill="var(--green-soft)"/>
  </svg>
  <div class="intro-left">
    <h2 class="section-h">Who <span class="green">We Are</span></h2>
    <p class="body-text">Tumble Scholars engages children in important topics, by utilising Parkour &amp; Acrobatics to captivate and enthrall todays youngest generation.</p>
    <ul class="checks">
      <li><span class="tick"><svg width="10" height="10" viewBox="0 0 10 10"><path d="M1.5 5.2l2.2 2.2L8.5 2.6" stroke="#fff" stroke-width="1.8" fill="none"/></svg></span>Live shows for every school</li>
      <li><span class="tick"><svg width="10" height="10" viewBox="0 0 10 10"><path d="M1.5 5.2l2.2 2.2L8.5 2.6" stroke="#fff" stroke-width="1.8" fill="none"/></svg></span>Messages kids remember</li>
      <li><span class="tick"><svg width="10" height="10" viewBox="0 0 10 10"><path d="M1.5 5.2l2.2 2.2L8.5 2.6" stroke="#fff" stroke-width="1.8" fill="none"/></svg></span>Lessons for before &amp; after</li>
    </ul>
    <div class="show-art" role="img" aria-label="Photo of performers tumbling in front of a school audience"></div>
  </div>
  <article class="tour-card">
    <p class="label">Now touring schools</p>
    <p class="product">Kindness-Shield Tumbling Tour</p>
    <p class="sub">Educating the Victim, Empowering the Bystander, and Enlightening the Bully</p>
    <p class="body-text">A high-energy show of flips, vaults and teamwork that shows students how to speak up, stand together and treat each other with care.</p>
    <p class="body-text">Each visit ends with a short talk and questions so the message stays with the class long after the final bow.</p>
    <a class="btn btn-sm" href="#">READ MORE</a>
  </article>
</section>

<section class="steps">
  <h2 class="steps-title">Book Now! in</h2>
  <p class="steps-sub">just 3 easy steps</p>
  <div class="step-row">
    <div class="step">
      <div class="step-art" role="img" aria-label="Illustration of a laptop with a booking form"></div>
      <p class="step-no">STEP 1</p>
      <h3 class="step-name">Send your enquiry</h3>
      <p class="body-text">Tell us about your school and class sizes.</p>
    </div>
    <div class="step featured">
      <div class="step-art" role="img" aria-label="Illustration of a calendar with show dates"></div>
      <p class="step-no">STEP 2</p>
      <h3 class="step-name">Choose your Show</h3>
      <p class="body-text">Pick a program and a date that suits you.</p>
    </div>
    <div class="step">
      <div class="step-art" role="img" aria-label="Illustration of a school hall ready for a show"></div>
      <p class="step-no">STEP 3</p>
      <h3 class="step-name">Enjoy the Show</h3>
      <p class="body-text">We arrive, set up and bring the energy.</p>
    </div>
  </div>
</section>

<section class="resources">
  <div class="browser">
    <div class="browser-bar"><span></span><span></span><span></span></div>
    <div class="browser-nav">Teachers Resources Portal</div>
    <div class="resource-photos" role="img" aria-label="Grid of photos showing lesson plans, workbooks and classroom activities"></div>
  </div>
  <div class="plant" role="img" aria-label="Illustration of a potted green plant"></div>
  <div class="resources-text">
    <h2 class="section-h">Teachers Resources</h2>
    <p class="body-text">Curriculum based resources for teachers including lesson plans, workbooks, and physical activities for before &amp; after the show.</p>
    <div class="subjects"><span>Mathematics</span><span>Science</span><span>PD/H/PE</span></div>
    <a class="btn btn-sm" href="#">LEARN MORE</a>
  </div>
</section>

<footer class="site-footer">
  <div class="footer-col footer-about">
    <div class="brand"><span class="brand-dot"></span>Tumble Scholars</div>
    <p class="body-text">Tumble Scholars brings tumbling shows and lessons on kindness to schools across the region.</p>
    <a class="btn btn-dark" href="#">BOOK NOW</a>
    <div class="socials"><span></span><span></span><span></span><span></span><span></span><span></span><span></span></div>
  </div>
  <div class="footer-col footer-contact">
    <h4 class="footer-h">Contact Detail</h4>
    <div class="contact-row">
      <svg width="12" height="14" viewBox="0 0 12 14"><path d="M6 0a5 5 0 0 1 5 5c0 3.6-5 9-5 9S1 8.6 1 5a5 5 0 0 1 5-5z" fill="var(--green)"/><circle cx="6" cy="5" r="1.8" fill="#fff"/></svg>
      <span>27 Market Lane, Suite 400,<br>Harbour Point, Glenmoor 40210,<br>Ashland</span>
    </div>
    <div class="contact-row">
      <svg width="12" height="12" viewBox="0 0 12 12"><path d="M2.5 0.5l2 2.5-1 1.5a7 7 0 0 0 4 4l1.5-1 2.5 2-1.5 2A10 10 0 0 1 0.5 2z" fill="var(--green)"/></svg>
      <span><b>+1 555 014 2290</b></span>
    </div>
    <div class="contact-row">
      <svg width="12" height="10" viewBox="0 0 12 10"><rect x="0.5" y="0.5" width="11" height="9" rx="1" fill="none" stroke="var(--green)"/><path d="M0.5 1l5.5 4.5L11.5 1" fill="none" stroke="var(--green)"/></svg>
      <span>hello@tumblescholars.example</span>
    </div>
  </div>
  <div class="footer-col footer-sitemap">
    <h4 class="footer-h">SITEMAP</h4>
    <ul class="sitemap">
      <li>Home</li><li>Teachers Portal</li>
      <li>About Us</li><li>Lesson Plans</li>
      <li>Our Program</li><li>Contact</li>
      <li>Our Shows</li><li>Terms of Service</li>
      <li>Book a Show</li><li>Privacy Policy</li>
    </ul>
  </div>
</footer>
<div class="bottom-bar"><span>&copy; Copyright</span><span>All rights reserved</span></div>

</body>
</html>
```